Dental Business Card

I need Dental oriented business cards.
On the front side -
- on the first line, my name:
Dr Marlo Vintner
- on the second line (just underneath):
Doctor of Dental Medicine
- on the third line, or underneath that or in a corner, I would like the address and phone number:
5182 Ch. Birchfield
Montreal QC H2T 4B9
514-629-5074
- other than that i would maybe like a logo of a tooth, but i want it to be subtle and very basic!
- I would like the card to be preferably black or dark grey-ish with the writing in white
On the other side -
- 2-3 lines with the possibility to write the next appointment the box with the lines should be white, with the rest of the card being black

```html
<!DOCTYPE html>
<html lang="en">
<head>
<meta charset="UTF-8">
<title>Dr Marlo Vintner – Business Card</title>
<link href="https://fonts.googleapis.com/css2?family=Raleway:wght@400&family=Lato:wght@400&display=swap" rel="stylesheet">
<style>
  :root {
    --page-bg: #2b2e33;
    --card-bg: #0b0b0c;
    --ink-light: #e9e9e9;
    --ink-muted: #8a8a8a;
    --slip-bg: #ededed;
    --slip-rule: #555555;
  }
  * { box-sizing: border-box; margin: 0; padding: 0; }
  html, body {
    width: 1200px; height: 900px; overflow: hidden;
    background: var(--page-bg);
  }
  .sheet {
    width: 1200px; height: 900px;
    display: flex; flex-direction: column;
    align-items: center; justify-content: center; gap: 48px;
  }
  .card {
    position: relative;
    width: 600px; height: 343px;
    background: var(--card-bg);
    border-radius: 26px;
    box-shadow: 0 14px 30px rgba(0,0,0,0.45);
    color: var(--ink-light);
  }
  .brand {
    position: absolute;
    display: flex; flex-direction: column; align-items: flex-end;
  }
  .brand-name {
    font-family: "Raleway", sans-serif;
    font-weight: 400;
    font-size: 40px;
    letter-spacing: 0.5px;
    color: var(--ink-light);
    line-height: 1;
  }
  .brand-title {
    font-family: "Raleway", sans-serif;
    font-size: 9.5px;
    letter-spacing: 2.6px;
    color: var(--ink-muted);
    margin-top: 5px;
    text-transform: uppercase;
  }
  .card-front .brand { left: 44px; top: 64px; }
  .contact {
    position: absolute; left: 330px; top: 200px;
    font-family: "Lato", sans-serif;
    font-size: 17px; line-height: 1.45;
    color: var(--ink-light);
    list-style: none;
  }
  .contact li { display: flex; align-items: flex-start; gap: 8px; }
  .contact .icon { width: 12px; height: 16px; margin-top: 4px; flex: none; }
  .contact .indent { padding-left: 20px; }
  .card-back .brand { right: 40px; top: 34px; }
  .appointment-label {
    position: absolute; right: 150px; top: 128px;
    font-family: "Lato", sans-serif;
    font-size: 13px; color: var(--ink-muted);
  }
  .appointment-slip {
    position: absolute; left: 32px; top: 150px;
    width: 536px; height: 160px;
    background: var(--slip-bg);
    padding: 26px 22px;
    display: flex; flex-direction: column; justify-content: space-between;
  }
  .appointment-slip .rule { height: 1px; background: var(--slip-rule); }
</style>
</head>
<body>
<main class="sheet">
  <section class="card card-front" aria-label="Card front">
    <div class="brand">
      <span class="brand-name">Marlo Vintner</span>
      <span class="brand-title">Doctor of Dental Medicine</span>
    </div>
    <ul class="contact">
      <li>
        <svg class="icon" viewBox="0 0 12 16" aria-hidden="true"><path d="M6 0C2.7 0 0 2.6 0 5.8 0 10 6 16 6 16s6-6 6-10.2C12 2.6 9.3 0 6 0zm0 8a2.2 2.2 0 1 1 0-4.4A2.2 2.2 0 0 1 6 8z" fill="#9a9a9a"/></svg>
        <span>5182 Ch. Birchfield</span>
      </li>
      <li class="indent">Montreal QC H2T 4B9</li>
      <li>
        <svg class="icon" viewBox="0 0 12 16" aria-hidden="true"><path d="M3 1l2 3-1.3 1.4c.7 2 1.8 3.6 3.4 4.9L8.6 9l3 2-1 3c-5.4-.6-9-5.4-9.4-11z" fill="#9a9a9a"/></svg>
        <span>514-629-5074</span>
      </li>
    </ul>
  </section>

  <section class="card card-back" aria-label="Card back">
    <div class="brand">
      <span class="brand-name">Marlo Vintner</span>
      <span class="brand-title">Doctor of Dental Medicine</span>
    </div>
    <span class="appointment-label">Next Appointment</span>
    <div class="appointment-slip">
      <div class="rule"></div>
      <div class="rule"></div>
      <div class="rule"></div>
      <div class="rule"></div>
    </div>
  </section>
</main>
</body>
</html>
```